Naturopath Practitioner Card Design

I am a naturopath needing a design for a business card mainly to show that I am a naturopath and have some contact details to give to prospective clients. I am open minded about the design and what is on the second side of the card whether it just be some artwork or space for details, appointment times etc. Naturopathy is the practice of natural medicine that uses a holistic approach and incorporates herbal and nutritional medicine.

Industry/Entity Type

Business

Contact Information for Business Card

Tom Welby NaturopathBHSc (Naturopathy) Member PHRA 0492 815 306 tom.welby@mailbright.com www.tomwelbynaturopathy.com.au

Requirements
Nice to have
• Would prefer some kind of original pattern/art work/logo rather than an image, not fussed if its very simple/basic
• I am open to any colour but think I would prefer a more earthy sandy clay etc type style than the greens that are commonly associated with naturopathy.
Should not have
• Don't really want to have generic stock images on it

```html
<!DOCTYPE html>
<html lang="en">
<head>
<meta charset="utf-8">
<title>Tom Welby Naturopath – Business Card</title>
<link rel="stylesheet" href="https://fonts.googleapis.com/css2?family=Arimo:wght@400;700&family=Noto+Serif:wght@700&display=swap">
<style>
  :root {
    --page: #ece9e4;
    --card: #ffffff;
    --ink: #1c1c1c;
    --pink: #c8166e;
    --pink-deep: #9e1556;
    --gold: #e0a516;
    --photo-light: #f4f2f0;
    --photo-skin: #e9cbb7;
    --stone: #3a3a3a;
    --lime: #a9dd3a;
    --dots: #333333;
  }
  * { box-sizing: border-box; margin: 0; padding: 0; }
  html, body { width: 1200px; height: 892px; overflow: hidden; }
  body {
    background: var(--page);
    font-family: "Arimo", Arial, sans-serif;
    color: var(--ink);
    position: relative;
  }
  .card {
    position: absolute;
    width: 700px;
    height: 400px;
    background: var(--card);
    box-shadow: 0 6px 18px rgba(0,0,0,.18);
    overflow: hidden;
  }
  .card--front { left: 250px; top: 26px; }
  .card--back  { left: 250px; top: 466px; background: linear-gradient(135deg, #ffffff 0%, #f3f1ef 60%, #e8e5e2 100%); }

  .card__art { position: absolute; inset: 0; width: 100%; height: 100%; }

  .contact {
    position: absolute;
    left: 44px;
    top: 168px;
  }
  .contact__name { font-size: 44px; font-weight: 700; line-height: 1; letter-spacing: -0.5px; }
  .contact__role { font-size: 24px; margin-top: 6px; }
  .contact__cred { font-size: 21px; margin-top: 4px; }
  .contact__list { list-style: none; margin-top: 14px; }
  .contact__item { display: flex; align-items: center; gap: 10px; font-size: 21px; margin-top: 4px; }
  .contact__icon { width: 16px; height: 16px; flex: none; }

  .appointment__title {
    position: absolute;
    top: 34px;
    right: 60px;
    font-family: "Noto Serif", Georgia, serif;
    font-weight: 700;
    font-size: 44px;
  }
  .appointment__fields { position: absolute; left: 50px; right: 60px; top: 130px; }
  .field { display: flex; align-items: flex-end; gap: 8px; font-size: 22px; font-weight: 700; height: 48px; }
  .field__line { flex: 1; border-bottom: 3px dotted var(--dots); margin-bottom: 6px; }
  .days { display: flex; gap: 26px; margin-top: 22px; font-size: 20px; }
  .day { display: flex; align-items: center; gap: 5px; }
  .day__box { width: 18px; height: 18px; border: 2px solid var(--ink); }
</style>
</head>
<body>

<section class="card card--front" aria-label="Business card front">
  <svg class="card__art" viewBox="0 0 700 400" aria-hidden="false">
    <defs>
      <linearGradient id="photoTone" x1="0" y1="0" x2="1" y2="1">
        <stop offset="0" stop-color="#f7f6f4"/>
        <stop offset="0.55" stop-color="#eed8c9"/>
        <stop offset="1" stop-color="#f5efea"/>
      </linearGradient>
      <linearGradient id="pinkTone" x1="0" y1="0" x2="1" y2="1">
        <stop offset="0" stop-color="var(--pink)"/>
        <stop offset="1" stop-color="var(--pink-deep)"/>
      </linearGradient>
    </defs>
    <rect class="photo" role="img" aria-label="Photo area: woman relaxing during a spa massage" x="0" y="0" width="700" height="400" fill="url(#photoTone)"/>
    <rect x="0" y="150" width="420" height="250" fill="#ffffff" opacity="0.55"/>
    <path d="M 290 400 C 440 330, 590 220, 700 70 L 700 400 Z" fill="#ffffff"/>
    <path d="M 305 400 C 455 335, 600 230, 700 88 L 700 400 Z" fill="var(--gold)"/>
    <path d="M 318 400 C 465 340, 608 240, 700 102 L 700 400 Z" fill="#ffffff"/>
    <path d="M 330 400 C 475 345, 615 250, 700 114 L 700 400 Z" fill="url(#pinkTone)"/>
    <rect role="img" aria-label="Illustration: hot stones and green candle" x="340" y="300" width="120" height="80" rx="30" fill="var(--stone)"/>
    <rect role="img" aria-label="Illustration: rolled spa towels" x="560" y="40" width="120" height="60" rx="20" fill="var(--lime)"/>
  </svg>

  <div class="contact">
    <h1 class="contact__name">Tom Welby</h1>
    <p class="contact__role">Naturopath</p>
    <p class="contact__cred">BHSc (Naturopathy) Member PHRA</p>
    <ul class="contact__list">
      <li class="contact__item">
        <svg class="contact__icon" viewBox="0 0 16 16"><rect width="16" height="16" fill="#222"/><path d="M4 3h3l1 3-2 1a7 7 0 0 0 3 3l1-2 3 1v3c-5 0-9-4-9-9z" fill="#fff"/></svg>
        0492 815 306
      </li>
      <li class="contact__item">
        <svg class="contact__icon" viewBox="0 0 16 16"><rect width="16" height="16" fill="#222"/><rect x="3" y="5" width="10" height="7" fill="none" stroke="#fff" stroke-width="1.4"/><path d="M3 5l5 4 5-4" fill="none" stroke="#fff" stroke-width="1.4"/></svg>
        tom.welby@mailbright.com
      </li>
    </ul>
  </div>
</section>

<section class="card card--back" aria-label="Business card back">
  <h2 class="appointment__title">Appointment</h2>
  <div class="appointment__fields">
    <div class="field">For: <span class="field__line"></span></div>
    <div class="field">Date: <span class="field__line"></span></div>
    <div class="field">Time: <span class="field__line"></span></div>
    <div class="days">
      <span class="day"><span class="day__box"></span>MON.</span>
      <span class="day"><span class="day__box"></span>TUE.</span>
      <span class="day"><span class="day__box"></span>WED.</span>
      <span class="day"><span class="day__box"></span>THUR.</span>
      <span class="day"><span class="day__box"></span>FRI.</span>
      <span class="day"><span class="day__box"></span>SAT.</span>
    </div>
  </div>
</section>

</body>
</html>
```